Book cover for a book on tactics, habits and directives learned from world class performers

The Steady Routines book is the first in a series of four books filled with proven tactics, habits and directives (i.e., what to do) that young, ambitious working professionals should be doing to make their life better. The first book is on foundational or keystone habits - that is, the habits that will help everyone upgrade their life and enable other great habits in their life (things such as waking up early in the morning or exercising)

The goal of the book is to stand out on the Orbello platform as a small thumbnail, as well as a 5 x 8 book.

The imagery should make the viewer feel that the book (and the author) are the authority in habits and developing habits.

The reader should feel that they must have this book if they know they should be developing successful habits but do not want to comb through hundreds of books just to find the one tactic or habit that they should be doing. It's important that the book "pops off the shelf" and catches the eye quickly.

The most important part of the design is that it sells, not that it looks well-designed. I am open to any image or illustration you choose though please consider the nice have I have listed below. Here are a few words that come to mind when thinking of my book: growth, self development, leadership, success, freedom, passion, motivation, young professional, accomplished, experience.

I like a bold color palette. I like bold titles that you know right away what the title is and what it is about, not too busy and with simple color schemes. 2 - 3 colors.

Books with covers I like:
- Night Venture by Dorian Flemwick
- Our Finest Season Yet by Gerald Pomfret
- The Fortune Outlook by Warren Ketterby

Target Market(s)

- Young 20 - 40 year old ambitious working professionals interested in self development and listen to podcasts of Lou Brandvik, Oscar Menderlin
- Just starting out management consultants

Colors

Designer to choose colors to be used in the design.

Requirements
Must have
• 'Steady Routines' title - first and foremost
• Author name - Lo Chen - probably on the bottom or somewhere
• Bold colour / colours or a graphic that is eye catching (and makes it different from other habits books on Orbello)
Nice to have
• Would like to have some sort of visual, colour or theme that can run through the four books - would be great to have a cover design that can be simply changed to depict the second, third or fourth book in the series - maybe the graphic or visual can be changed with some colours, etc. but with the overall feel looking similar so that people can see that it's part of the same book series

```html
<!DOCTYPE html>
<html lang="en">
<head>
<meta charset="utf-8">
<title>Steady Routines — Book Cover</title>
<link rel="stylesheet" href="https://fonts.googleapis.com/css2?family=Bebas+Neue&display=swap">
<style>
  :root {
    --backdrop: #111111;
    --cover-paper: #fafafa;
    --title-blue: #1f6fb4;
    --title-red: #d9403f;
    --author-green: #2f7d3c;
    --art-money: #c9cdb0;
    --art-money-deep: #b9c0a0;
    --art-mailbox: #d8231f;
    --art-mailbox-deep: #c41c18;
  }
  html, body {
    margin: 0;
    padding: 0;
    width: 1200px;
    height: 1200px;
    overflow: hidden;
    background: var(--backdrop);
  }
  .canvas {
    position: relative;
    width: 1200px;
    height: 1200px;
    display: flex;
    align-items: center;
    justify-content: center;
  }
  .book-cover {
    width: 700px;
    height: 1120px;
    background: var(--cover-paper);
    display: block;
  }
  .cover-title,
  .cover-author {
    font-family: "Bebas Neue", "Oswald", sans-serif;
  }
  .title-line-top { fill: var(--title-blue); }
  .title-line-main { fill: var(--title-red); }
  .cover-author { fill: var(--author-green); }
</style>
</head>
<body>
  <main class="canvas">
    <svg class="book-cover" viewBox="0 0 700 1120" xmlns="http://www.w3.org/2000/svg">
      <defs>
        <linearGradient id="artTones" x1="0" y1="0" x2="1" y2="0">
          <stop offset="0" stop-color="var(--art-money)"/>
          <stop offset="0.5" stop-color="var(--art-money-deep)"/>
          <stop offset="0.6" stop-color="var(--art-mailbox)"/>
          <stop offset="1" stop-color="var(--art-mailbox-deep)"/>
        </linearGradient>
      </defs>

      <rect class="cover-paper" width="700" height="1120" fill="var(--cover-paper)"/>

      <g class="cover-title">
        <text class="title-line-top" x="58" y="262" font-size="205" textLength="588" lengthAdjust="spacingAndGlyphs">STEADY</text>
        <text class="title-line-main" x="52" y="500" font-size="290" textLength="596" lengthAdjust="spacingAndGlyphs">ROUTINES</text>
      </g>

      <g class="cover-art" role="img" aria-label="Photograph of a shiny red mailbox lying on its side with a pile of crumpled banknotes spilling out of its open door">
        <ellipse cx="340" cy="712" rx="290" ry="138" fill="url(#artTones)" opacity="0.85"/>
      </g>

      <text class="cover-author" x="62" y="1045" font-size="215" textLength="568" lengthAdjust="spacingAndGlyphs">LO CHEN</text>
    </svg>
  </main>
</body>
</html>
```